依頼詳細
全体の基本としては、黒色を希望しますが、良い案があればお任せしたいと思います。
弊社のブランドロゴ(添付画像のB-5のデザイン)MELVOTAをさりげなくつけてください。
今までのパッケージのデザインも参考までに添付しておきます。
記載項目
蓋のサイズ210×60×18(添付画像参照)です。
底のサイズ205×55×35、底の部分は、黒色等の無地でもOKです。
希望イメージ
シンプル 複雑
単色 カラフル
暗い 明るい
日常 高級
遊び心 厳粛
未来的 伝統的
女性的 男性的
希望する色
全体としては黒色ですが、カラフル華やかに
納品ファイル
• イラストレーター形式 (.ai)
補足説明
繊細で透明感があり、カラフルな感じにしてもらえたらと思います。「GLASS PEN」と文字、またはグラスペンの形をデザインしたものが蓋の部分にあると嬉しいです。

色のバランス、インパクトです。

多くのご提案ありがとうございます。

```html
<!DOCTYPE html>
<html lang="en">
<head>
<meta charset="UTF-8">
<title>MELVOTA Glass Pen Lid</title>
<link rel="stylesheet" href="https://fonts.googleapis.com/css2?family=Montserrat:wght@400;500&display=swap">
<style>
  :root {
    --page: #ffffff;
    --lid: #000000;
    --ink: #ffffff;
    --sky: #1a9ad6;
    --indigo: #2b3a98;
    --magenta: #e2207f;
    --red: #e5262a;
    --orange: #f39a1c;
    --yellow: #ffec00;
    --green: #17a04a;
  }
  html, body {
    margin: 0;
    padding: 0;
    width: 1200px;
    height: 2564px;
    overflow: hidden;
    background: var(--page);
  }
  .canvas {
    position: relative;
    width: 1200px;
    height: 2564px;
    background: var(--page);
  }
  .lid {
    position: absolute;
    left: 352px;
    top: 192px;
    width: 520px;
    height: 2140px;
    background: var(--lid);
  }
  .rainbow-band {
    position: absolute;
    left: 0;
    width: 100%;
    height: 176px;
    display: flex;
  }
  .rainbow-band--top { top: 0; }
  .rainbow-band--bottom { bottom: 0; }
  .rainbow-band span { flex: 1; }
  .c-sky { background: var(--sky); }
  .c-indigo { background: var(--indigo); }
  .c-magenta { background: var(--magenta); }
  .c-red { background: var(--red); }
  .c-orange { background: var(--orange); }
  .c-yellow { background: var(--yellow); }
  .c-green { background: var(--green); }

  .brand {
    position: absolute;
    top: 214px;
    left: 0;
    width: 100%;
    display: flex;
    flex-direction: column;
    align-items: center;
    gap: 12px;
  }
  .brand-mark {
    width: 30px;
    height: 30px;
    border: 3px solid var(--ink);
    border-radius: 50%;
  }
  .brand-name {
    font-family: "Montserrat", sans-serif;
    font-weight: 500;
    font-size: 18px;
    letter-spacing: 3px;
    color: var(--ink);
  }
  .pen-art {
    position: absolute;
    left: 214px;
    top: 390px;
    width: 92px;
    height: 1440px;
  }
  .product-name {
    position: absolute;
    top: 1864px;
    left: 0;
    width: 100%;
    text-align: center;
    font-family: "Montserrat", sans-serif;
    font-weight: 400;
    font-size: 34px;
    letter-spacing: 12px;
    padding-left: 12px;
    box-sizing: border-box;
    color: var(--ink);
  }
</style>
</head>
<body>
  <div class="canvas">
    <div class="lid">
      <div class="rainbow-band rainbow-band--top">
        <span class="c-sky"></span><span class="c-indigo"></span><span class="c-magenta"></span><span class="c-red"></span><span class="c-orange"></span><span class="c-yellow"></span><span class="c-green"></span>
      </div>

      <div class="brand">
        <div class="brand-mark"></div>
        <div class="brand-name">MELVOTA</div>
      </div>

      <svg class="pen-art" viewBox="0 0 92 1440" role="img" aria-label="Line illustration of a twisted glass dip pen in rainbow colours">
        <defs>
          <linearGradient id="pen-tones" x1="0" y1="0" x2="0" y2="1">
            <stop offset="0" stop-color="#1a9ad6"/>
            <stop offset="0.35" stop-color="#2b3a98"/>
            <stop offset="0.55" stop-color="#e2207f"/>
            <stop offset="0.7" stop-color="#e5262a"/>
            <stop offset="0.82" stop-color="#f39a1c"/>
            <stop offset="0.92" stop-color="#ffec00"/>
            <stop offset="1" stop-color="#17a04a"/>
          </linearGradient>
        </defs>
        <rect x="0" y="0" width="92" height="1440" rx="46" fill="url(#pen-tones)" opacity="0.55"/>
      </svg>

      <div class="product-name">GLASS PEN</div>

      <div class="rainbow-band rainbow-band--bottom">
        <span class="c-sky"></span><span class="c-indigo"></span><span class="c-magenta"></span><span class="c-red"></span><span class="c-orange"></span><span class="c-yellow"></span><span class="c-green"></span>
      </div>
    </div>
  </div>
</body>
</html>
```